Powerpoint presentation about personal finance

Investing 4$ per day is what has been required to become a millionaire by investing in the stock market from 1965 to 2015. Yet only 1% of the population is millionaire. This presentation is about the most common causes why people do not build significant wealth through their life. We intend to educate people with this presentation, but also build trust so they become client of our wealth management firm. Feel free to send us any question about this project.
Updates

Reason: I have uploaded the logo source file and an updated PPT file. Thanks

Target Market(s)

People with a willingness to save money between the age of 20 to 50 years old

Industry/Entity Type

Finance

Font styles to use
Sans Serif

Requirements
Must have
• We are looking at uniforming the design throughout the presentation with nice, classic tone colors, large font size as it needs to be visible 3 meters apart. The content of the presentation will be updated regularly.
Should not have
• cartoon style, not serious

```html
<!DOCTYPE html>
<html lang="fr">
<head>
<meta charset="utf-8">
<title>Présentation – Finances personnelles</title>
<link href="https://fonts.googleapis.com/css2?family=Lato:wght@300;400;700&family=Montserrat:wght@600;800&display=swap" rel="stylesheet">
<style>
  :root{
    --ink:#1f2a2e;
    --white:#ffffff;
    --brand-ink:#2c3a40;
    --chart-blue:#3c78c3;
    --chart-green:#4b5e22;
    --grid:#e4e4e4;
    --conclusion-bg:#e2e2e2;
    --accent-red:#c0283f;
    --accent-blue:#2a6aa8;
  }
  *{box-sizing:border-box;margin:0;padding:0}
  html,body{width:1063px;height:1200px;overflow:hidden;background:var(--white)}
  body{position:relative;font-family:"Lato",sans-serif;color:var(--ink)}
  .slide{position:absolute;overflow:hidden}

  /* Slide 1 — intro */
  .slide-intro{left:0;top:0;width:531px;height:400px}
  .slide-intro .photo{position:absolute;inset:0;
    background:linear-gradient(180deg,#cfe6ee 0%,#8fc3d6 30%,#4f96b3 55%,#3f7f8a 75%,#7aa54a 90%,#b6c75a 100%)}
  .brand{position:absolute;left:356px;top:26px;width:158px;height:55px;background:rgba(255,255,255,.92);
    display:flex;align-items:center;justify-content:center;gap:9px;box-shadow:0 0 12px 6px rgba(255,255,255,.7)}
  .brand-mark{width:12px;height:12px;background:var(--brand-ink);flex:none}
  .brand-name{font-weight:700;font-size:17px;color:var(--brand-ink);letter-spacing:.5px}
  .intro-text{position:absolute;left:21px;top:232px;font-weight:300;font-size:28.5px;line-height:34.5px;color:var(--white)}

  /* Slide 2 — dreams */
  .slide-dreams{left:531px;top:0;width:532px;height:400px}
  .slide-dreams .photo{position:absolute;inset:0;
    background:linear-gradient(180deg,#6b6e71 0%,#595c57 28%,#3e4a34 55%,#4f5f2e 80%,#77833e 100%)}
  .dreams-band{position:absolute;left:0;top:124px;width:532px;height:91px;
    background:linear-gradient(90deg,#8c8fc0 0%,#a8a6cf 45%,#9c9a5a 70%,#8a7a3a 100%);
    display:flex;align-items:center;justify-content:center}
  .dreams-band h2{font-weight:300;font-size:34px;color:var(--white);padding-left:20px}

  /* Slide 3 — chart */
  .slide-chart{left:0;top:400px;width:531px;height:398px;background:var(--white)}
  .chart-header{position:absolute;left:0;top:0;width:531px;height:131px;
    background:linear-gradient(180deg,#6d7c8c 0%,#8f95a0 35%,#6a6e62 60%,#2f4a2f 85%,#385a33 100%)}
  .chart-title{position:absolute;left:10px;top:71px;font-size:20px;line-height:24px;color:var(--white)}
  .chart{position:absolute;left:0;top:131px}
  .chart text{font-family:"Lato",sans-serif}

  /* Slide 4 — fear of losing */
  .slide-fear{left:531px;top:400px;width:532px;height:398px;background:var(--white)}
  .timeline{position:absolute;left:0;top:0;width:185px;height:398px;
    background:linear-gradient(180deg,#f1f2f0 0%,#e6ebe2 45%,#d7dfc9 75%,#cfd7bc 100%)}
  .step{position:absolute;left:16px;display:flex;align-items:center;gap:18px}
  .step-num{width:29px;height:29px;border-radius:50%;border:1.5px solid #333;background:var(--white);
    display:flex;align-items:center;justify-content:center;font-size:12px;flex:none}
  .step.is-active .step-num{background:#111;color:var(--white)}
  .step-label{font-size:10px;line-height:11px;color:#444;width:110px;font-weight:300}
  .timeline-line{position:absolute;left:30px;top:30px;width:1.5px;height:336px;background:#333}
  .fear-body{position:absolute;left:201px;top:30px;width:305px}
  .fear-body h3{font-size:16px;font-weight:700;padding-bottom:3px;border-bottom:1.5px solid #222;margin-bottom:28px}
  .fear-body p{font-size:14px;line-height:18.5px;margin-bottom:17px}

  /* Slide 5 — conclusion */
  .slide-conclusion{left:0;top:798px;width:532px;height:398px;background:var(--conclusion-bg)}
  .conclusion-title{position:absolute;left:0;top:30px;width:532px;text-align:center;font-family:"Montserrat",sans-serif;
    font-weight:800;font-size:68px;letter-spacing:2px;
    background:linear-gradient(90deg,#7f98a8 0%,#c9a27a 20%,#e0653a 35%,#8e7a86 50%,#d8704a 65%,#b58a7a 80%,#9fb0a8 100%);
    -webkit-background-clip:text;background-clip:text;color:transparent}
  .conclusion-text{position:absolute;left:0;top:147px;width:532px;text-align:center;font-family:"Montserrat",sans-serif;
    font-weight:600;font-size:27px;line-height:34.5px;color:#3a2a30}
  .conclusion-text .red{color:var(--accent-red)}
  .conclusion-text .blue{color:var(--accent-blue)}
</style>
</head>
<body>

<section class="slide slide-intro">
  <div class="photo" role="img" aria-label="Photo de montagnes bleutées et de vallée verdoyante"></div>
  <div class="brand">
    <span class="brand-mark"></span>
    <span class="brand-name">Sommetra</span>
  </div>
  <p class="intro-text">L’idéal n’est-il pas d’avoir<br>suffisamment d’argent<br>et d’être en santé afin<br>de pouvoir réaliser nos rêves?</p>
</section>

<section class="slide slide-dreams">
  <div class="photo" role="img" aria-label="Photo de forêt de sapins en montagne sous un ciel brumeux"></div>
  <div class="dreams-band"><h2>Quels sont vos rêves?</h2></div>
</section>

<section class="slide slide-chart">
  <div class="chart-header" role="img" aria-label="Photo d'un sommet enneigé au-dessus d'une forêt"></div>
  <p class="chart-title">Investissement équivalent à 4$ par jour<br>en actions* de 1965 à 2015</p>
  <svg class="chart" width="531" height="267" viewBox="0 0 531 267">
    <g stroke="var(--grid)" stroke-width="0.7">
      <line x1="124" y1="7" x2="440" y2="7"/><line x1="124" y1="46.5" x2="440" y2="46.5"/>
      <line x1="124" y1="86" x2="440" y2="86"/><line x1="124" y1="125.5" x2="440" y2="125.5"/>
      <line x1="124" y1="165" x2="440" y2="165"/><line x1="124" y1="204.5" x2="440" y2="204.5"/>
      <line x1="124" y1="244" x2="440" y2="244"/>
    </g>
    <g font-size="4.5" fill="#777" text-anchor="end">
      <text x="116" y="9">1 200 000 $</text><text x="116" y="48.5">1 000 000 $</text>
      <text x="116" y="88">800 000 $</text><text x="116" y="127.5">600 000 $</text>
      <text x="116" y="167">400 000 $</text><text x="116" y="206.5">200 000 $</text>
      <text x="116" y="246">- $</text>
    </g>
    <g font-size="4.5" fill="#777" text-anchor="end">
      <text transform="translate(126,248) rotate(-90)">1965</text>
      <text transform="translate(157,248) rotate(-90)">1970</text>
      <text transform="translate(188,248) rotate(-90)">1975</text>
      <text transform="translate(220,248) rotate(-90)">1980</text>
      <text transform="translate(251,248) rotate(-90)">1985</text>
      <text transform="translate(282,248) rotate(-90)">1990</text>
      <text transform="translate(314,248) rotate(-90)">1995</text>
      <text transform="translate(345,248) rotate(-90)">2000</text>
      <text transform="translate(376,248) rotate(-90)">2005</text>
      <text transform="translate(408,248) rotate(-90)">2010</text>
      <text transform="translate(439,248) rotate(-90)">2015</text>
    </g>
    <line x1="124" y1="244" x2="437" y2="229" stroke="var(--chart-green)" stroke-width="1.5"/>
    <polyline fill="none" stroke="var(--chart-blue)" stroke-width="1.5" stroke-linejoin="round"
      points="124,244 186.6,242 217.9,236 249.2,224 268,214 280.5,212 293,199 305.5,197 318,165 330.5,116 336.8,90 343,115 355.5,153 361.8,125 368,116 380.6,100 386.8,94 393,151 405.6,112 411.9,112 418,93 424.5,47 430.7,23 437,24"/>
    <text x="333" y="48" font-size="9" font-weight="700" fill="var(--chart-blue)">Valeur finale:</text>
    <text x="333" y="60" font-size="9" font-weight="700" fill="var(--chart-blue)">1,114,000$</text>
    <text x="328" y="207" font-size="9" font-weight="700" fill="var(--chart-green)">Montant épargné:</text>
    <text x="328" y="219" font-size="9" font-weight="700" fill="var(--chart-green)">74,460$</text>
  </svg>
</section>

<section class="slide slide-fear">
  <div class="timeline" role="img" aria-label="Photo pâle de paysage de montagne en automne">
    <span class="timeline-line"></span>
    <div class="step" style="top:16px"><span class="step-num">1</span><span class="step-label">Ne pas épargner!</span></div>
    <div class="step is-active" style="top:64px"><span class="step-num">2</span><span class="step-label">La peur de perdre</span></div>
    <div class="step" style="top:111px"><span class="step-num">3</span><span class="step-label">Avoir une vision à court terme</span></div>
    <div class="step" style="top:159px"><span class="step-num">4</span><span class="step-label">L’accès à l’information pertinente</span></div>
    <div class="step" style="top:208px"><span class="step-num">5</span><span class="step-label">Le manque de notions financières</span></div>
    <div class="step" style="top:256px"><span class="step-num">6</span><span class="step-label">Les frais</span></div>
    <div class="step" style="top:304px"><span class="step-num">7</span><span class="step-label">Les impôts</span></div>
    <div class="step" style="top:352px"><span class="step-num">8</span><span class="step-label">L’augmentation du coût de la vie</span></div>
  </div>
  <div class="fear-body">
    <h3>La peur de perdre...</h3>
    <p>En 1973 et 1974, la valeur des actions américaines diminue de 40%.</p>
    <p>Un investisseur qui avait investi 4$ par jours depuis 1965 a vu son portefeuille passé de 13,300$ à 9,500$.</p>
    <p>Pris de panique, il vend toutes ses actions pour arrêter l’hémorragie.</p>
    <p>En 1975, les actions américaines augmentent de 37%. Maintenant tout excité après une telle performance, l’investisseur réinvesti ses 9,500$ l’année suivante.</p>
  </div>
</section>

<section class="slide slide-conclusion">
  <h2 class="conclusion-title">CONCLUSION</h2>
  <p class="conclusion-text">Parmi tous les facteurs<br>qui nuisent<br>financièrement aux individus,<br>le <span class="red">seul</span> que nous ne<br>pouvons vous<br><span class="blue">aider,</span> c’est l’inaction<span class="red">!</span></p>
</section>

</body>
</html>
```